Business Card Design Project For Moving Company

Hello,

We need the business card to be 2 sided and we were thinking to use the logo on the front of the card (see file 1 attached) and the text "logo" (see file 2 attached) in the back of the card. We're looking for a powerful design that will help us build our brand, as our company is new.
We are a full service moving company (no storage) located in San Diego, CA, USA. The design should communicate to our potential customers that we have the highest level of service, customer satisfaction is our number one goal, our team is professional and efficient.

Thank you,

Dorn
Updates

Project Deadline Extended
Reason: We would like to have more time to provide feedback for the designs already submitted. Thank you, Dorn

Industry/Entity Type

Moving Company

Requirements
Must have
• Front of the card must have the following text and logo:
Haulbright, Inc
Residential And Commercial
Local And Long Distance
Address: 7312 Quillmont Rd, #146,
San Diego, CA, 92784
P: 855-372-LIFT (5438)
F: 858-529-4407
info@haul-bright.com
www.haul-bright.com

Back of the card must have the following text and text "logo" (file 2 attached):

The best compliment we can ever receive is a referral from our clients.

```html
<!DOCTYPE html>
<html lang="en">
<head>
<meta charset="utf-8">
<title>Haulbright Business Cards</title>
<link rel="stylesheet" href="https://fonts.googleapis.com/css2?family=Arimo:wght@400;700&display=swap">
<style>
  :root {
    --backdrop: #3b3b3b;
    --card: #f4f4f4;
    --red: #d42a2a;
    --charcoal: #3a3a3a;
    --ink: #2b2b2b;
    --white: #ffffff;
  }
  * { margin: 0; padding: 0; box-sizing: border-box; }
  html, body { width: 1200px; height: 1000px; overflow: hidden; }
  body {
    background: var(--backdrop);
    font-family: "Arimo", Arial, sans-serif;
    color: var(--ink);
    position: relative;
  }
  .card {
    position: absolute;
    background: var(--card);
    border-radius: 14px;
    overflow: hidden;
  }
  .card--landscape { left: 125px; top: 350px; width: 530px; height: 300px; }
  .card--portrait { left: 783px; top: 235px; width: 302px; height: 527px; }

  .wordmark {
    position: absolute;
    font-weight: 700;
    color: var(--red);
    letter-spacing: -1px;
    white-space: nowrap;
  }
  .card--landscape .wordmark { left: 0; width: 100%; top: 48px; text-align: center; font-size: 58px; }
  .card--portrait .wordmark { left: 0; width: 100%; top: 120px; text-align: center; font-size: 40px; }

  .ribbon { position: absolute; left: 0; top: 0; }
  .ribbon-label {
    position: absolute;
    color: var(--white);
    font-size: 14px;
    font-weight: 700;
    white-space: nowrap;
  }

  .contact { position: absolute; font-size: 11.5px; line-height: 16px; }
  .label { color: var(--red); font-weight: 700; }

  .portrait-phones {
    position: absolute; left: 0; width: 100%; top: 366px;
    text-align: center; font-size: 17px; line-height: 24px;
  }
  .portrait-details {
    position: absolute; left: 0; width: 100%; top: 443px;
    text-align: center; font-size: 12px; line-height: 24.5px;
  }
  .portrait-details b { font-weight: 700; }
</style>
</head>
<body>

<section class="card card--landscape" aria-label="Card front">
  <div class="wordmark">HAULBRIGHT</div>

  <svg class="ribbon" width="530" height="300" viewBox="0 0 530 300" aria-hidden="true">
    <polygon points="0,152 283,152 255,181 0,181" fill="var(--red)"/>
    <polygon points="275,177 530,177 530,203 245,203" fill="var(--charcoal)"/>
  </svg>
  <div class="ribbon-label" style="left:23px; top:158px;">RESIDENTIAL AND COMMERCIAL</div>
  <div class="ribbon-label" style="right:25px; top:183px;">LOCAL AND LONG DISTANCE</div>

  <div class="contact" style="left:23px; top:246px;">
    7312 Quillmont Rd, #146<br>San Diego, CA, 92784
  </div>
  <div class="contact" style="left:181px; top:246px;">
    <span class="label">PHONE:</span> 855-372-LIFT (5438)<br>
    <span class="label">FAX:</span> 858-529-4407
  </div>
  <div class="contact" style="left:383px; top:246px;">
    info@haul-bright.com<br>www.haul-bright.com
  </div>
</section>

<section class="card card--portrait" aria-label="Card back">
  <div class="wordmark">HAULBRIGHT</div>

  <svg class="ribbon" width="302" height="527" viewBox="0 0 302 527" aria-hidden="true">
    <polygon points="0,260 256,260 282,274 256,288 0,288" fill="var(--charcoal)"/>
    <polygon points="0,293 256,293 282,307 256,322 0,322" fill="var(--red)"/>
  </svg>
  <div class="ribbon-label" style="left:17px; top:266px;">RESIDENTIAL AND COMMERCIAL</div>
  <div class="ribbon-label" style="left:29px; top:299px;">LOCAL AND LONG DISTANCE</div>

  <div class="portrait-phones">
    <span class="label">PHONE:</span> 855-372-LIFT (5438)<br>
    <span class="label">FAX:</span> 858-529-4407
  </div>
  <div class="portrait-details">
    7312 Quillmont Rd, #146, San Diego, CA, 92784<br>
    Email: info@haul-bright.com<br>
    www.<b>haul-bright</b>.com
  </div>
</section>

</body>
</html>
```